Investment Business - Biz Card Design

Using the attached logo files, please create a superior business card design for Tarnwell Holdings.

The "back" of the card should feature the logo (either in colour, or white/black over a feature colour)

The "front" of the card should feature: name, email, and phone

The design should be minimal and clean.

Target Market(s)

Business owners who need our investment services.

Industry/Entity Type

Business

```html
<!DOCTYPE html>
<html lang="en">
<head>
<meta charset="utf-8">
<title>Tarnwell Holdings – Business Card</title>
<link rel="stylesheet" href="https://fonts.googleapis.com/css2?family=Cinzel:wght@500;600&family=EB+Garamond:wght@400&family=Michroma&display=swap">
<style>
  :root {
    --page: #ffffff;
    --card-edge: #0e0e0e;
    --card-mid: #1f1f1f;
    --card-glow: #363636;
    --name-blue: #1877f2;
    --text-white: #ffffff;
    --mark-grey: #5a5a5c;
    --tile-top: #ffffff;
    --tile-bottom: #cfcfcf;
    --icon-blue: #1e5fa8;
  }
  * { margin: 0; padding: 0; box-sizing: border-box; }
  html, body {
    width: 1200px; height: 1000px; overflow: hidden;
    background: var(--page);
  }
  .business-card {
    position: absolute;
    left: 106px; top: 174px;
    width: 1039px; height: 647px;
    background: radial-gradient(ellipse at 45% 45%, var(--card-glow) 0%, var(--card-mid) 55%, var(--card-edge) 100%);
    overflow: hidden;
  }
  .holder-name {
    position: absolute;
    left: 94px; top: 52px;
    font-family: "Cinzel", serif;
    font-weight: 500;
    font-size: 60px;
    letter-spacing: 8px;
    color: var(--name-blue);
    text-shadow: 0 2px 3px rgba(0,0,0,0.8);
    white-space: nowrap;
  }
  .contact-row {
    position: absolute;
    left: 98px;
    display: flex; align-items: center;
  }
  .contact-row.email { top: 177px; }
  .contact-row.phone { top: 346px; }
  .icon-tile {
    width: 93px; height: 91px;
    border-radius: 14px;
    background: linear-gradient(var(--tile-top), var(--tile-bottom));
    box-shadow: 0 3px 6px rgba(0,0,0,0.6);
    display: flex; align-items: center; justify-content: center;
  }
  .phone .icon-tile { width: 90px; height: 88px; }
  .contact-text {
    color: var(--text-white);
    text-shadow: 0 2px 3px rgba(0,0,0,0.8);
    white-space: nowrap;
  }
  .email .contact-text {
    margin-left: 33px;
    font-family: "EB Garamond", serif;
    font-size: 56px;
    margin-top: -16px;
  }
  .phone .contact-text {
    margin-left: 40px;
    font-family: "Michroma", sans-serif;
    font-size: 31px;
    letter-spacing: 3px;
    margin-top: -12px;
  }
  .company-mark {
    position: absolute;
    right: 54px; bottom: 48px;
    font-family: "Cinzel", serif;
    font-weight: 600;
    font-size: 46px;
    line-height: 1.05;
    text-align: right;
    color: var(--mark-grey);
  }
</style>
</head>
<body>
  <main class="business-card">
    <h1 class="holder-name">Dilan Weraketh</h1>

    <div class="contact-row email">
      <div class="icon-tile">
        <svg width="66" height="46" viewBox="0 0 66 46" aria-hidden="true">
          <rect x="2" y="2" width="62" height="42" fill="#fff" stroke="var(--icon-blue)" stroke-width="3"/>
          <path d="M2 2 L33 26 L64 2 M2 44 L26 21 M64 44 L40 21" fill="none" stroke="var(--icon-blue)" stroke-width="3"/>
        </svg>
      </div>
      <span class="contact-text">info@tarnwell.com</span>
    </div>

    <div class="contact-row phone">
      <div class="icon-tile">
        <svg width="64" height="52" viewBox="0 0 64 52" aria-hidden="true">
          <path d="M4 16 Q4 4 32 4 Q60 4 60 16 L60 20 L46 20 L46 14 L18 14 L18 20 L4 20 Z" fill="var(--icon-blue)"/>
          <path d="M20 18 L44 18 L56 48 L8 48 Z" fill="var(--icon-blue)"/>
          <g fill="#fff">
            <rect x="25" y="26" width="3" height="3"/><rect x="30.5" y="26" width="3" height="3"/><rect x="36" y="26" width="3" height="3"/>
            <rect x="25" y="32" width="3" height="3"/><rect x="30.5" y="32" width="3" height="3"/><rect x="36" y="32" width="3" height="3"/>
            <rect x="25" y="38" width="3" height="3"/><rect x="30.5" y="38" width="3" height="3"/><rect x="36" y="38" width="3" height="3"/>
          </g>
        </svg>
      </div>
      <span class="contact-text">+94 71 5550184</span>
    </div>

    <div class="company-mark">Tarnwell<br>Holdings</div>
  </main>
</body>
</html>
```